"Global Leadership & Talent Development Firm" needs a website upgrade

Website Design Project is intended to find a vendor to update and provide maintenance for my website: www.Brightpath7Gains.com. I am looking for a vendor who is an expert with WordPress and eCommerce plugin.

Website Requirements
www.Brightpath7Gains.com

• Media Library (review)- Add video/utube
• Others (plug-ins)
1) eCommerce ability
a) Must have the ability to charge for the eLearning courses
i) Handle credit card processing
ii) Ability to handle yearly subscriptions
iii) Ability to process credits/refunds

Website Updates Assessment Page:
• Totally MORV- Distributor Information
• 4 Crew Patterns Assessment & logo
• Steering Quest- 360 Assessment
• Emotional Intelligence Assessment
Home & Tool Pages:
• K7V License and certification
• PulseCore Trainer
• 4 Crew Patterns training
Client & Contact Pages
• Update Client list
• Update testimonials
Speaker Page Update
Website Add on E-Commerce to sell products
• K7V Certification Program
• PulseCore tools & technology
• Totally MoRV Assessment Distributor
• 4 Crew Pattern Distributor

See attached document describing the updates.

Target Market(s)

Small-Large Business and Corporations
Public Sector Organizations

Industry/Entity Type

Leadership

Number of Pages Required

5+ page

Font styles to use
Other font styles liked:
• www.brightpath7gains.com

Requirements
Must have
• Wordpress expertise
• E-Commerce plugin expertise
• Website Maintenance capability
Nice to have
• Easy access to transfer documents and get feedback/suggestions on the best wording for presenting the information onto my site for each of the pages
Should not have
• Focus on changing the current design of my site

```html
<!DOCTYPE html>
<html lang="en">
<head>
<meta charset="utf-8">
<title>Brightpath7Gains – Developing Leadership Talent &amp; Succession</title>
<link href="https://fonts.googleapis.com/css2?family=Open+Sans:wght@400;600;700&display=swap" rel="stylesheet">
<style>
:root{
  --red:#d6131b;
  --orange:#f0a535;
  --dark:#2c2c2c;
  --darker:#1f1f1f;
  --text:#444;
  --white:#fff;
  --panel:#f1f1f1;
  --gold:#f2b233;
  --partner:#666;
}
*{box-sizing:border-box;margin:0;padding:0}
html,body{width:1200px;height:2514px;overflow:hidden}
body{font-family:"Open Sans",Arial,sans-serif;color:var(--text);background:var(--white);position:relative}
.abs{position:absolute}

/* header */
.brand{left:80px;top:28px}
.brand-name{font-size:34px;font-weight:400;color:#555;line-height:1}
.brand-tag{font-size:12px;color:#555;margin-top:6px}
.toplink{top:23px;font-size:11px;color:#444;white-space:nowrap}
.toplink-sep{top:21px;font-size:11px;color:#bbb}
.member-btn{left:994px;top:14px;width:126px;height:30px;background:var(--red);color:#fff;font-size:11px;font-weight:600;display:flex;align-items:center;justify-content:center;border-radius:3px}
.search{left:793px;top:60px;width:295px;height:25px;border:1px solid #bbb}
.search-btn{left:1088px;top:60px;width:30px;height:25px;background:var(--red);display:flex;align-items:center;justify-content:center}
.phone{left:838px;top:93px;font-size:16px;font-weight:700;color:var(--red)}
.wish{left:974px;top:98px;font-size:11px;color:var(--red)}
.cart{left:1042px;top:96px;display:flex;align-items:center;gap:6px;font-size:11px;color:var(--red)}

/* nav */
.nav{left:0;top:129px;width:1200px;height:50px;background:linear-gradient(#fbd88f,#f2ad3d)}
.nav-link{top:14px;font-size:16px;color:#333;white-space:nowrap}

/* hero */
.hero{left:0;top:179px;width:1200px;height:563px;background:linear-gradient(160deg,#4a5870 0%,#c98a5a 45%,#f0b36a 60%,#7a5040 80%,#3a2a2a 100%)}
.hero-title{left:80px;top:250px;color:#111;line-height:1.1}
.hero-title .l1{font-size:44px;font-weight:400}
.hero-title .l2{font-size:54px;font-weight:700;color:var(--red)}
.hero-title .l2 span{color:#111;font-weight:400;font-size:44px}
.hero-title .l3{font-size:56px;font-weight:700}
.hero-box{left:80px;top:461px;width:503px;height:92px;background:rgba(40,40,40,.82);border-radius:4px;color:#fff;font-size:17px;line-height:1.3;padding:10px 18px}
.hero-btn{left:84px;top:585px;width:154px;height:37px;background:var(--red);color:#fff;font-size:12px;display:flex;align-items:center;justify-content:center;border-radius:2px}
.dot{width:16px;height:16px;border-radius:50%;border:2px solid #fff;top:604px}
.dot.on{background:var(--gold);border-color:var(--gold)}
.share{left:1176px;top:368px;display:flex;flex-direction:column;gap:2px}
.share i{display:block;width:24px;height:26px;background:#6d7b8f}

/* welcome */
.darkband{left:0;top:742px;width:1200px;height:356px;background:var(--dark)}
.welcome{left:80px;top:669px;width:1041px;height:271px;background:var(--white);display:flex}
.welcome-left{width:238px;padding:28px 20px}
.welcome-left h2{font-size:21px;font-weight:400;color:#222;line-height:1.25}
.welcome-left h2 b{font-weight:700}
.rule{width:66px;height:4px;background:var(--red);margin:12px 0 22px}
.welcome-left h3{font-size:15px;font-weight:400;color:var(--red)}
.welcome-left p{font-size:12px;line-height:1.3;color:#333}
.signup{display:flex;margin-top:18px}
.signup .field{width:176px;height:27px;border:1px solid #bbb;font-size:10px;color:#555;padding:6px}
.signup .go{width:33px;height:27px;background:var(--red);color:#fff;font-size:11px;font-weight:700;display:flex;align-items:center;justify-content:center;margin-left:4px}
.welcome-mid{width:456px;background:var(--panel);padding:26px 20px;font-size:14px;line-height:1.4;color:#555;text-align:justify}
.welcome-right{flex:1;padding:30px 20px}
.video{width:307px;height:211px;background:linear-gradient(135deg,#8c7a70,#c4c0ba,#6d6a66);position:relative}
.play{position:absolute;left:97px;top:71px;width:114px;height:70px;background:var(--red);display:flex;align-items:center;justify-content:center}

/* stats */
.stat{top:966px;width:200px;text-align:center;color:#fff}
.stat .num{font-size:33px;color:var(--gold);line-height:1;margin-top:10px}
.stat .lbl{font-size:17px;font-weight:700}

/* offer */
.offer{left:0;top:1098px;width:1200px;height:550px;background:linear-gradient(#4b4b4b,#8a8a8a 40%,#3a3a3a)}
.offer-title{left:0;top:1130px;width:1200px;text-align:center;color:#fff;font-size:21px}
.offer-title i{display:block;width:66px;height:3px;background:#fff;margin:10px auto 0}
.offer-icon{top:1205px;width:64px;height:64px}
.card{top:1289px;width:235px;height:258px;background:#fff;border-radius:3px;padding:18px 16px;text-align:center}
.card h4{font-size:16px;font-weight:700;color:var(--red);margin-bottom:26px}
.card p{font-size:12.5px;line-height:1.3;color:#444}
.card-btn{top:1487px;width:110px;height:42px;background:var(--red);color:#fff;font-size:12px;display:flex;align-items:center;justify-content:center;clip-path:polygon(0 0,86% 0,100% 100%,0 100%)}

/* corporate */
.corp{left:0;top:1648px;width:598px;height:274px;background:var(--orange);padding:42px 80px}
.corp h3{font-size:21px;font-weight:400;color:#222}
.corp .rule{margin:10px 0 18px}
.corp p{font-size:14px;line-height:1.35;color:#222}
.corp-btn{display:inline-flex;margin-top:24px;width:129px;height:37px;background:#2b2b2b;color:#fff;font-size:12px;align-items:center;justify-content:center}
.partner{font-size:26px;font-weight:400;color:var(--partner);white-space:nowrap}
.badge{left:1004px;top:1774px;width:46px;height:76px;background:#ddd}

/* team */
.team-title{left:80px;top:1944px;font-size:22px;color:#222}
.team-title b{color:var(--red);font-weight:700}
.team-title i{display:block;width:45px;height:4px;background:var(--red);margin-top:10px}
.member{top:2011px;width:298px;height:322px}
.member .info{position:absolute;left:0;bottom:14px;width:100%;text-align:center;color:#fff;font-size:15px;line-height:1.2}

/* testimonials */
.testi{left:0;top:2333px;width:1200px;height:126px;background:var(--darker)}
.testi-title{left:80px;top:2348px;color:#fff;font-size:21px;font-weight:400}
.testi-rule{left:80px;top:2384px;width:128px;height:3px;background:var(--red)}
.testi-sub{left:80px;top:2398px;color:#ddd;font-size:12.5px;line-height:1.25;width:160px}
.vbar{left:277px;top:2350px;width:2px;height:92px;background:#555}
.avatar{left:308px;top:2359px;width:74px;height:74px;border-radius:50%;background:#8a8a8a;border:3px solid #fff}
.quote{left:414px;top:2366px;width:690px;font-size:12.5px;color:#ccc;line-height:1.35}

/* footer */
.footer{left:0;top:2459px;width:1200px;height:55px;background:#ececec;display:flex;align-items:center;padding-left:80px;font-size:12.5px;color:#444}
.footer span{margin-right:18px}
.footer span:first-child{color:var(--red)}
.copy{left:960px;top:2482px;font-size:10px;color:var(--red)}
</style>
</head>
<body>

<!-- header -->
<div class="abs brand">
  <div class="brand-name">Brightpath7Gains</div>
  <div class="brand-tag">Developing Leadership Talent &amp; Succession</div>
</div>
<span class="abs toplink" style="left:731px">Log In or Register</span>
<span class="abs toplink-sep" style="left:834px">|</span>
<span class="abs toplink" style="left:848px">About Us</span>
<span class="abs toplink-sep" style="left:906px">|</span>
<span class="abs toplink" style="left:918px">My Account</span>
<div class="abs member-btn">BECOME A MEMBER</div>
<div class="abs search"></div>
<div class="abs search-btn"><svg width="14" height="14" viewBox="0 0 14 14"><circle cx="6" cy="6" r="4.5" fill="none" stroke="#fff" stroke-width="2"/><line x1="9.5" y1="9.5" x2="13" y2="13" stroke="#fff" stroke-width="2"/></svg></div>
<div class="abs phone">(555) 014-2290</div>
<div class="abs wish">Wish List</div>
<div class="abs cart"><svg width="16" height="13" viewBox="0 0 16 13"><path d="M0 1h3l2 8h8l2-6H4" fill="none" stroke="#999" stroke-width="1.4"/><circle cx="6" cy="11.5" r="1.2" fill="#999"/><circle cx="12" cy="11.5" r="1.2" fill="#999"/></svg><b>0</b><span style="color:#999;margin-left:10px">▾</span></div>

<nav class="abs nav">
  <span class="abs nav-link" style="left:85px">Home</span>
  <span class="abs nav-link" style="left:183px">Approach</span>
  <span class="abs nav-link" style="left:307px">Tools</span>
  <span class="abs nav-link" style="left:401px">Assessments</span>
  <span class="abs nav-link" style="left:550px">Clients</span>
  <span class="abs nav-link" style="left:652px">Consultants</span>
  <span class="abs nav-link" style="left:794px">Speaking</span>
  <span class="abs nav-link" style="left:913px">Blog</span>
  <span class="abs nav-link" style="left:999px">Contact</span>
</nav>

<!-- hero -->
<div class="abs hero" role="img" aria-label="Photo of two climbers helping each other up a rock at sunset"></div>
<div class="abs hero-title">
  <div class="l1">Behind Every</div>
  <div class="l2">GOOD RESULT <span>is a</span></div>
  <div class="l3">GREAT INSIGHT</div>
</div>
<div class="abs hero-box">it's a platform for a selected community of innovators. We provide the space, the community and the service you need to succeed.</div>
<div class="abs hero-btn">EXPLORE OUR STORY</div>
<div class="abs dot on" style="left:1045px"></div>
<div class="abs dot" style="left:1073px"></div>
<div class="abs dot" style="left:1101px"></div>
<div class="abs share"><i></i><i></i><i></i><i></i><i></i></div>

<!-- welcome -->
<div class="abs darkband"></div>
<section class="abs welcome">
  <div class="welcome-left">
    <h2>Welcome to<br><b>brightpath7gains</b></h2>
    <div class="rule"></div>
    <h3>Stay Updated with us</h3>
    <p>Get access to sale &amp; price alerts as well as exclusive promo codes by signing up to our newsletter.</p>
    <div class="signup"><div class="field">Type your Email here</div><div class="go">GO&gt;</div></div>
  </div>
  <div class="welcome-mid">Looking for a boxed approach? You won't find it here. Our approach is an exchange; an exchange of dynamic listening and deliberate question asking. We ultimately identify the key leadership and talent factors that influence your organization's issues and successes. Then we apply our breadth of experience in working with companies like yours and people like you to develop a model of your company's leadership culture, language, symbols and values. As partners, we collaborate with you to mold, customize, and implement an application uniquely designed for your people, values, and systems, and strategies.</div>
  <div class="welcome-right">
    <div class="video" role="img" aria-label="Video still of people on escalators in an office atrium">
      <div class="play"><svg width="26" height="30" viewBox="0 0 26 30"><path d="M0 0l26 15L0 30z" fill="#fff"/></svg></div>
    </div>
  </div>
</section>

<div class="abs stat" style="left:274px">
  <svg width="28" height="32" viewBox="0 0 28 32"><path d="M14 2a10 10 0 0 1 10 10c0 8-10 18-10 18S4 20 4 12A10 10 0 0 1 14 2z" fill="none" stroke="#fff" stroke-width="2.4"/><circle cx="14" cy="12" r="4" fill="none" stroke="#fff" stroke-width="2.4"/></svg>
  <div class="num">05</div><div class="lbl">Campuses</div>
</div>
<div class="abs stat" style="left:463px">
  <svg width="36" height="32" viewBox="0 0 36 32"><circle cx="18" cy="9" r="5" fill="none" stroke="#fff" stroke-width="2.2"/><circle cx="7" cy="13" r="3.5" fill="none" stroke="#fff" stroke-width="2"/><circle cx="29" cy="13" r="3.5" fill="none" stroke="#fff" stroke-width="2"/><path d="M8 28a10 10 0 0 1 20 0M1 28a6 6 0 0 1 9-6M35 28a6 6 0 0 0-9-6" fill="none" stroke="#fff" stroke-width="2.2"/></svg>
  <div class="num">156</div><div class="lbl">Talents</div>
</div>
<div class="abs stat" style="left:689px">
  <svg width="30" height="34" viewBox="0 0 30 34"><circle cx="15" cy="12" r="9.5" fill="none" stroke="#fff" stroke-width="2.4"/><circle cx="15" cy="12" r="4" fill="none" stroke="#fff" stroke-width="2"/><path d="M8 19l-4 12 5-2 3 4 3-11M22 19l4 12-5-2-3 4-3-11" fill="none" stroke="#fff" stroke-width="2"/></svg>
  <div class="num">2656</div><div class="lbl">Club Members</div>
</div>

<!-- offer -->
<div class="abs offer" role="img" aria-label="Black and white aerial photo of a city skyline"></div>
<div class="abs offer-title">What <b>We offer</b><i></i></div>

<svg class="abs offer-icon" style="left:156px" viewBox="0 0 64 64"><g fill="#fff"><circle cx="32" cy="22" r="7"/><circle cx="16" cy="28" r="5.5"/><circle cx="48" cy="28" r="5.5"/><path d="M21 50c0-9 5-16 11-16s11 7 11 16zM6 50c0-7 4-13 10-13 3 0 5 1 6 3-3 3-5 7-5 10zM58 50c0-7-4-13-10-13-3 0-5 1-6 3 3 3 5 7 5 10z"/></g><g stroke="#fff" stroke-width="2"><line x1="32" y1="4" x2="32" y2="10"/><line x1="20" y1="8" x2="23" y2="13"/><line x1="44" y1="8" x2="41" y2="13"/></g></svg>
<svg class="abs offer-icon" style="left:438px" viewBox="0 0 64 64"><g fill="#fff"><circle cx="32" cy="30" r="7"/><circle cx="32" cy="10" r="5"/><circle cx="12" cy="40" r="5"/><circle cx="52" cy="40" r="5"/><circle cx="32" cy="54" r="5"/></g><g stroke="#fff" stroke-width="2.5"><line x1="32" y1="15" x2="32" y2="23"/><line x1="16" y1="38" x2="26" y2="33"/><line x1="48" y1="38" x2="38" y2="33"/><line x1="32" y1="37" x2="32" y2="49"/></g></svg>
<svg class="abs offer-icon" style="left:703px" viewBox="0 0 64 64"><g fill="#fff"><circle cx="20" cy="18" r="6"/><circle cx="40" cy="16" r="6"/><path d="M8 42c0-9 5-15 12-15s10 4 11 8l-6 7zM33 28c2-3 5-4 7-4 7 0 12 6 12 13h-9"/></g><circle cx="36" cy="38" r="8" fill="none" stroke="#fff" stroke-width="3"/><line x1="42" y1="44" x2="52" y2="54" stroke="#fff" stroke-width="4"/></svg>
<svg class="abs offer-icon" style="left:970px" viewBox="0 0 64 64"><g fill="#fff"><path d="M32 4l9 10h-6v9h-6v-9h-6z"/><path d="M32 60l9-10h-6v-9h-6v9h-6z"/><path d="M4 32l10-9v6h9v6h-9v6z"/><path d="M60 32l-10-9v6h-9v6h9v6z"/></g></svg>

<article class="abs card" style="left:80px"><h4>Coaching7Gains™</h4><p>Most leaders believe that setting ambitious goals and merely providing regular corrective feedback will create the results they need. Research and experience prove that this is NOT enough...</p></article>
<article class="abs card" style="left:349px"><h4>Managing7Gains™</h4><p>Management training must equip and empower managers to drive better results, make better decisions, and develop strong performers and teams...</p></article>
<article class="abs card" style="left:615px"><h4>Mentoring7Gains™</h4><p>Research shows that employees entering the workplace today want work to afford them the opportunity to make new friends, learn new skills and connect to a larger purpose...</p></article>
<article class="abs card" style="left:883px"><h4>Core Outlook Gauge®</h4><p>Achieving results is about closing gaps and turning strategy into execution and creativity into innovation. The bridge over these gaps is Collaboration. And the columns of this bridge are mind sets.</p></article>
<div class="abs card-btn" style="left:64px">LEARN MORE</div>
<div class="abs card-btn" style="left:331px">LEARN MORE</div>
<div class="abs card-btn" style="left:597px">LEARN MORE</div>
<div class="abs card-btn" style="left:866px">LEARN MORE</div>

<!-- corporate -->
<section class="abs corp">
  <h3>Corporate <b>Innovation</b></h3>
  <div class="rule"></div>
  <p>We help the corporate world innovate by discovering and bringing the latest digital trends and technologies into their businesses. Additionally, we share our expertise in collaborative office design and corporate culture.</p>
  <div class="corp-btn">FIND OUT MORE</div>
</section>
<div class="abs partner" style="left:632px;top:1696px">Lumora</div>
<div class="abs partner" style="left:816px;top:1696px">Typeway</div>
<div class="abs partner" style="left:950px;top:1696px">Totally MoRV</div>
<div class="abs partner" style="left:632px;top:1800px">PulseCore</div>
<div class="abs partner" style="left:826px;top:1800px">Relatix</div>
<div class="abs badge"></div>

<!-- team -->
<div class="abs team-title">Inside <b>The team</b><i></i></div>
<div class="abs member" style="left:0;background:linear-gradient(#bdbdbd,#7a6a60)" role="img" aria-label="Portrait photo of team member">
  <div class="info"><b>Lena Varsk</b><br>@lena<br>Cofounder &amp; CEO</div></div>
<div class="abs member" style="left:300px;background:linear-gradient(#c4c4c4,#6f7a88)" role="img" aria-label="Portrait photo of team member">
  <div class="info"><b>Owen Pell</b><br>@owen_pell<br>MD at Business</div></div>
<div class="abs member" style="left:600px;background:linear-gradient(#cfcfcf,#b04a55)" role="img" aria-label="Portrait photo of team member">
  <div class="info"><b>Mira Dalton</b><br>@mira<br>International Development Manager</div></div>
<div class="abs member" style="left:902px;background:linear-gradient(#bcbcbc,#555)" role="img" aria-label="Portrait photo of team member">
  <div class="info"><b>Tomas Reed</b><br>@tomas<br>VP External relations</div></div>

<!-- testimonials -->
<div class="abs testi"></div>
<h3 class="abs testi-title">Testimonials</h3>
<div class="abs testi-rule"></div>
<div class="abs testi-sub">Reputation is everything for us</div>
<div class="abs vbar"></div>
<div class="abs avatar" role="img" aria-label="Portrait of client giving testimonial"></div>
<p class="abs quote">Grenadier jackfish arowana temperate perch bonytongue seamoth sea devil longfin Alaska blackfish yellow weaver. Elephant fish great white shark. Sed ut perspiciatis unde omnis iste natus error sit voluptatem accusantium doloremque laudantium, totam rem aperiam, eaque ipsa quae ab...</p>

<!-- footer -->
<footer class="abs footer"><span>Home</span><span>Approach</span><span>Tools</span><span>Assessments</span><span>Clients</span><span>Consultants</span><span>Speaking</span><span>Blog</span><span>Contact</span></footer>
<div class="abs copy">Copyright 2015 © brightpath7gains.com</div>

</body>
</html>
```